Drywall plastering business card design

Attached is my new logo and a picture of my current business card. I would like my new logo incorporated in to the business card and also my website which is:
www.ridgecrestwallfinishers.co.nz
Industry/Entity Type
Business
Contact Information for Business Card
I would like a picture of my van and my new logo on my new business card. See attached files for pictures of my old business card, van picture and logo.
Colors
0555a3
ffffff
Requirements
Must have
- New logo, Van, contact info

```html
<!DOCTYPE html>
<html lang="en">
<head>
<meta charset="utf-8">
<title>Ridgecrest Wall Finishers – Business Card</title>
<link rel="stylesheet" href="https://fonts.googleapis.com/css2?family=Lato:wght@400;700;900&display=swap">
<style>
  :root {
    --brand-blue: #0555a3;
    --deep-blue: #04468a;
    --white: #ffffff;
    --backdrop: #e9ecef;
    --sky: #8fc3ea;
    --hills: #6f7f86;
    --grass: #5d7a3c;
  }
  * { margin: 0; padding: 0; box-sizing: border-box; }
  html, body {
    width: 1200px; height: 900px; overflow: hidden;
    background: var(--backdrop);
    font-family: "Lato", Arial, sans-serif;
  }
  .card {
    position: absolute; left: 100px; top: 170px;
    width: 1000px; height: 560px;
    background: var(--white);
    overflow: hidden;
    box-shadow: 0 14px 40px rgba(0,0,0,.25);
  }
  .card-photo {
    position: absolute; left: 0; top: 0; width: 100%; height: 270px;
    background: linear-gradient(180deg, var(--sky) 0%, #cfe4f3 45%, var(--hills) 62%, var(--grass) 100%);
  }
  .card-shapes { position: absolute; inset: 0; }
  .brand {
    position: absolute; left: 70px; top: 330px;
    display: flex; align-items: center; gap: 16px;
  }
  .brand-mark { width: 26px; height: 26px; background: var(--white); }
  .brand-name {
    color: var(--white); font-weight: 900; font-size: 34px;
    line-height: 1; letter-spacing: .5px;
  }
  .contact {
    position: absolute; right: 60px; top: 268px;
    text-align: right; color: var(--white);
  }
  .contact-name { font-weight: 900; font-size: 24px; letter-spacing: 1px; }
  .contact-role { font-size: 20px; margin-bottom: 18px; }
  .contact-line {
    display: flex; justify-content: flex-end; align-items: center;
    gap: 12px; font-size: 19px; margin-bottom: 10px;
  }
  .contact-line svg { width: 18px; height: 18px; flex: none; }
  .tagline {
    position: absolute; left: 0; right: 0; top: 470px;
    text-align: center; color: var(--white);
    font-weight: 700; font-size: 24px; letter-spacing: .3px;
  }
</style>
</head>
<body>
  <div class="card">
    <div class="card-photo" role="img" aria-label="Photo of the company's white van parked above a lake with mountains behind"></div>

    <svg class="card-shapes" viewBox="0 0 1000 560" preserveAspectRatio="none" aria-hidden="true">
      <path d="M0 250 Q 420 200 1000 80 L1000 560 L0 560 Z" fill="var(--white)"/>
      <path d="M0 270 Q 420 225 1000 105 L1000 500 Q 600 400 0 500 Z" fill="var(--brand-blue)"/>
      <path d="M0 520 Q 560 430 1000 520 L1000 560 L0 560 Z" fill="var(--white)"/>
    </svg>

    <div class="brand">
      <span class="brand-mark"></span>
      <span class="brand-name">Ridgecrest<br>Wall Finishers</span>
    </div>

    <div class="contact">
      <div class="contact-name">DANIEL HART</div>
      <div class="contact-role">Proprietor</div>
      <div class="contact-line">027 555 01 42
        <svg viewBox="0 0 24 24"><path fill="#fff" d="M6.6 10.8a15 15 0 0 0 6.6 6.6l2.2-2.2a1 1 0 0 1 1-.25 11.4 11.4 0 0 0 3.6.57 1 1 0 0 1 1 1V20a1 1 0 0 1-1 1A17 17 0 0 1 3 4a1 1 0 0 1 1-1h3.5a1 1 0 0 1 1 1c0 1.25.2 2.45.57 3.57a1 1 0 0 1-.25 1z"/></svg>
      </div>
      <div class="contact-line">hello@ridgecrestwallfinishers.co.nz
        <svg viewBox="0 0 24 24"><path fill="#fff" d="M3 5h18v14H3z"/><path d="M3 5l9 7 9-7" fill="none" stroke="var(--brand-blue)" stroke-width="2"/></svg>
      </div>
      <div class="contact-line">www.ridgecrestwallfinishers.co.nz
        <svg viewBox="0 0 24 24"><circle cx="10" cy="10" r="6" fill="none" stroke="#fff" stroke-width="2.5"/><path d="M14.5 14.5L21 21" stroke="#fff" stroke-width="3" stroke-linecap="round"/></svg>
      </div>
    </div>

    <div class="tagline">Large Jobs or Small - Always Quality Assured</div>
  </div>
</body>
</html>
```